Consulting Firm stationery design

Now that the MakerHive has given us a new logo we'll now need to have all our stationery designed. So we're asking for this community to help us once again.We're looking to get from you Letterheads (Header and Footer, suitable to be applied on a .docx format. Vectors are required but keep this in mind), Envelopes (Front and Back designs, back is not a must but desirable depending on your design), 9"x 12" Pocket Folders (consider design for front and back, also for pockets as well), Business Cards.An elegant design is a must have, mostly for Folders and Envelopes. The idea with this two is to stand out from others when they're handed over. Ideas are welcomed, we were thinking maybe on some texturing simulation for these.Folders will have 3 addresses and contact information. Envelopes will have 1 address and contact information.Brand Manual attached. vendaluxo logo has been copyrighted already. I'm also attaching the current stationary designs (these never got to be out for production but was going to be before we made the brand changes); Pocker folders page 1 to 4 (pages 2 and 4 are the pocket designs), Pages 5 and 6 (6 is the back of the envelope), Pages 7 and 8 (8 is the back of the business card). No letterhead within these designs as it just had the logo and address.

Industry/Entity Type

Business Consultant

Font styles to use
Serif
Sans Serif

Requirements
Must have
• Elegance
Nice to have
• Modern looking out of common

```html
<!DOCTYPE html>
<html lang="es">
<head>
<meta charset="utf-8">
<title>Vendaluxo SRL – Letterhead</title>
<link rel="stylesheet" href="https://fonts.googleapis.com/css2?family=Questrial&display=swap">
<style>
  :root {
    --ink: #32333e;
    --brand-blue: #0580bb;
    --paper: #fdfdfd;
  }
  * { margin: 0; padding: 0; box-sizing: border-box; }
  html, body { width: 848px; height: 1200px; overflow: hidden; background: var(--paper); }
  .letterhead {
    position: relative;
    width: 848px;
    height: 1200px;
    background: var(--paper);
    font-family: "Questrial", "Century Gothic", sans-serif;
    color: var(--ink);
  }
  .brand-mark {
    position: absolute;
    top: 96px;
    right: 101px;
    display: flex;
    align-items: center;
    gap: 8px;
  }
  .brand-mark__name {
    font-size: 38px;
    line-height: 1;
    color: var(--ink);
    letter-spacing: -0.5px;
  }
  .brand-mark__dot {
    width: 16px;
    height: 16px;
    border-radius: 50%;
    background: var(--brand-blue);
  }
  .company-address {
    position: absolute;
    left: 99px;
    top: 1093px;
  }
  .company-address__name {
    font-size: 14px;
    font-weight: 700;
    letter-spacing: 4.4px;
    color: var(--brand-blue);
    line-height: 1;
    margin-bottom: 5px;
  }
  .company-address__line,
  .company-contact__line {
    font-size: 11.3px;
    line-height: 15.4px;
  }
  .company-contact {
    position: absolute;
    left: 321px;
    top: 1109px;
  }
  .company-contact__label {
    display: inline-block;
    width: 14px;
  }
  .footer-band {
    position: absolute;
    bottom: 0;
    height: 29px;
  }
  .footer-band--dark {
    left: 392px;
    width: 338px;
    background: var(--ink);
    border-top-left-radius: 29px;
  }
  .footer-band--blue {
    left: 736px;
    right: 0;
    background: var(--brand-blue);
  }
</style>
</head>
<body>
  <div class="letterhead">
    <header class="brand-mark">
      <span class="brand-mark__name">vendaluxo</span>
      <span class="brand-mark__dot"></span>
    </header>

    <footer>
      <div class="company-address">
        <p class="company-address__name">VENDALUXO SRL</p>
        <p class="company-address__line">Cedro Business Plaza</p>
        <p class="company-address__line">Avenida Los Laureles 42, Naco</p>
        <p class="company-address__line">Santo Domingo, Rep. Dominicana</p>
      </div>
      <div class="company-contact">
        <p class="company-contact__line"><span class="company-contact__label">T</span>(809) 555 0143 ext. 201</p>
        <p class="company-contact__line"><span class="company-contact__label">M</span>(809) 555 0178</p>
        <p class="company-contact__line"><span class="company-contact__label">E</span>info@vendaluxo.do</p>
      </div>
      <div class="footer-band footer-band--dark"></div>
      <div class="footer-band footer-band--blue"></div>
    </footer>
  </div>
</body>
</html>
```